Business card Zottelgarten

Business card is for a self-employed dog trainer with own dog school. Name and logo of the dog school are available. Color specifications as well. The design should be classy and minimalist, but also modern. An already existing idea would be: Front: Only the logo Back: Contact data

Font styles to use
Serif
Sans Serif
Other font styles liked:
• Trajan Pro

Colors
f78f20

Requirements
Must have
• Name: Margit Wendler-Rasch Title: Dipl. Dog Trainer Contain my logo Follow my font and color preferences (see files)

```html
<!DOCTYPE html>
<html lang="de">
<head>
<meta charset="utf-8">
<title>Zottelgarten – Business Card</title>
<link rel="stylesheet" href="https://fonts.googleapis.com/css2?family=Cinzel:wght@400&family=Montserrat:wght@400&display=swap">
<style>
  :root {
    --orange: #f78f20;
    --white: #ffffff;
    --paper: #ececec;
    --ink-grey: #555555;
    --card-w: 660px;
    --card-h: 384px;
  }
  * { box-sizing: border-box; margin: 0; padding: 0; }
  html, body {
    width: 1200px;
    height: 1200px;
    overflow: hidden;
    background: var(--paper);
  }
  .sheet {
    position: relative;
    width: 1200px;
    height: 1200px;
  }
  .card {
    position: absolute;
    left: 270px;
    width: var(--card-w);
    height: var(--card-h);
    overflow: hidden;
    box-shadow: 0 6px 24px rgba(0,0,0,0.10);
  }
  .card--front { top: 160px; background: var(--orange); }
  .card--back  { top: 656px; background: var(--white); }

  /* Front */
  .brand {
    position: absolute;
    inset: 0;
    display: flex;
    flex-direction: column;
    align-items: center;
    justify-content: center;
    color: var(--white);
  }
  .brand__mark {
    width: 132px;
    height: 132px;
    border-radius: 50%;
    background: var(--white);
    margin-bottom: -6px;
  }
  .brand__name {
    font-family: "Cinzel", serif;
    font-weight: 400;
    font-size: 40px;
    letter-spacing: 0.04em;
    line-height: 1;
    margin-top: 18px;
  }
  .brand__web {
    font-family: "Montserrat", sans-serif;
    font-size: 10px;
    letter-spacing: 0.55em;
    text-transform: uppercase;
    margin-top: 8px;
  }

  /* Back */
  .back__panel {
    position: absolute;
    left: 0; top: 0;
    width: 396px;
    height: 100%;
    background: var(--orange);
  }
  .contact {
    position: absolute;
    right: 300px;
    top: 58px;
    text-align: left;
    color: var(--white);
    font-family: "Cinzel", serif;
  }
  .contact__name {
    font-size: 22px;
    letter-spacing: 0.02em;
    line-height: 1.2;
  }
  .contact__title {
    font-size: 14px;
    letter-spacing: 0.03em;
    margin-top: 2px;
  }
  .contact__rule {
    position: absolute;
    left: 378px;
    top: 62px;
    height: 60px;
    border-left: 2px dotted var(--white);
  }
  .back__mark {
    position: absolute;
    left: 326px;
    top: 160px;
    width: 140px;
    height: 140px;
    border-radius: 50%;
    background: var(--white);
    border: 10px solid var(--orange);
  }
  .back__web {
    position: absolute;
    left: 560px;
    top: 50%;
    transform: translate(-50%, -50%) rotate(-90deg);
    white-space: nowrap;
    font-family: "Montserrat", sans-serif;
    font-size: 11px;
    letter-spacing: 0.6em;
    text-transform: uppercase;
    color: var(--ink-grey);
  }
</style>
</head>
<body>
  <main class="sheet">
    <section class="card card--front" aria-label="Card front">
      <div class="brand">
        <div class="brand__mark"></div>
        <div class="brand__name">Zottelgarten</div>
        <div class="brand__web">www.zottelgarten.ch</div>
      </div>
    </section>

    <section class="card card--back" aria-label="Card back">
      <div class="back__panel"></div>
      <div class="contact">
        <p class="contact__name">Margit Wendler-Rasch</p>
        <p class="contact__title">Dipl. Dog Trainer</p>
      </div>
      <div class="contact__rule"></div>
      <div class="back__mark"></div>
      <p class="back__web">www.zottelgarten.ch</p>
    </section>
  </main>
</body>
</html>
```